Webbanner-Design für Konferenz- und Messeformat
Zielgruppe
VOLMARKTIS - forum for smart commerce || Das virtuelle Konferenz- und Messeformat, wenn es um das Thema Digitalisierung geht.
Mit diesem Format adressieren wir Aussteller, Referenten und Besucher, welche sich um die Digitalisierung von Kundenprojekten kümmern. Dies mit Produkten, Lösungen aber auch Beratungsleistungen. Die Zielgruppe unserer Besucher sind die Unternehmen, welche nach geeigneten Lösungen suchen und Ihr Business digitaler gestalten möchten, somit auch entsprechende Projekte auf der Agenda haben.
Daher sind unsere Hauptthemen der Veranstaltung: Industrie 4.0, digital future, digital Workplace, IT Infrastruktur. Eine detaillierte thematische Gliederung finden Sie anbei.
Das besondere an der VOLMARKTIS ist, dass wir kein Konferenz- und Messeformat im „klassischen“ physischen Sinne sind. Unser Format ist voll digitalisiert und wird virtuell durchgeführt. Dies hat für die Aussteller die wesentlichen Vorteile:
- Kostengünstige Teilnahme als Referent und Aussteller
- Keine Reiseaufwendungen
- Weniger Standpersonal
- Größere Reichweite für Besucher mit geringerem Budget
- Größere Skalierbarkeit in Bezug auf Besuchergruppen
- Statistische Erfassung des Besucherverhalten und somit die Erzeugung von vorqualifizierten Leads
- Möglichkeit neue Zielgruppen zu erreichen, welche immer mehr von den traditionellen Messeformaten fernbleiben
-- Insbesondere durch die flexible Teilnahme an den Veranstaltungstagen und in der OnDemand Phase
Die hier zu erstellenden Banner sollen zwei Zwecke erfüllen. Zum einen wird es im Mai ein Mailing durch unseren Partner plovo geben, wo wir die Veranstaltung gegenüber potentiellen Ausstellern, Referenten und Sponsoren bewerben. Dieser Banner soll jedoch ebenso auf der zugehörigen plovo Eventseite als Header dienen. In selbigen Zusammenhang ist das Icon für die plovo Event Seiten zu gestalten.
Daher benötigen wir ein Design für den Header im..
Aufgabenstellung
Das sind die Bannergrößen für das Mailing
Megabanner desktop: 600 x 250 px
Megabanner mobil: 400 x 300 px
Das ist die größe für den Header / Banner auf der plovo Event Seite
Abmessungen: mind. 984 x 311 Pixel (B x H)
Das ist die größe für das Icon auf der plovo Event Seite
Quadratisches Bild mit mind. 256 x 256 Pixel (B x H), max. 3200 x 3200 Pixel
Dateiformat: JPG, PNG, BMP oder GIF + Quelldatei
Größe für den Upload: max. 5 MB
Farbmodus: RGB (kein CMYK etc.)
Bitte geben Sie bitte die zusätzlichen Kosten für evtl. benötigte Stockmedien an.

```html
<!DOCTYPE html>
<html lang="de">
<head>
<meta charset="utf-8">
<title>VOLMARKTIS – Bannerset</title>
<link href="https://fonts.googleapis.com/css2?family=Raleway:wght@400;500;600;700&display=swap" rel="stylesheet">
<style>
  :root {
    --navy: #0b2a66;
    --blue: #124a94;
    --sky: #2a8fd6;
    --accent: #36a9ea;
    --band: #8fb6da;
    --white: #ffffff;
    --red: #d9393f;
    --red-dark: #a81f26;
  }
  * { box-sizing: border-box; margin: 0; padding: 0; }
  html, body { width: 1200px; height: 1193px; overflow: hidden; background: var(--white); }
  body { position: relative; font-family: "Raleway", sans-serif; color: var(--white); }

  .banner { position: absolute; overflow: hidden; }
  .banner-bg { position: absolute; inset: 0; width: 100%; height: 100%; }

  .header { left: 0; top: 0; width: 1200px; height: 382px; }
  .mega-desktop { left: 122px; top: 439px; width: 740px; height: 308px; }
  .mega-mobile { left: 122px; top: 779px; width: 493px; height: 370px; }

  .wordmark { position: absolute; display: flex; align-items: center; font-weight: 600; letter-spacing: 0.01em; line-height: 1; white-space: nowrap; }
  .wordmark-square { display: inline-block; background: var(--accent); margin-right: 0.14em; width: 0.42em; height: 0.42em; }

  .tagline { position: absolute; font-weight: 400; white-space: nowrap; line-height: 1; }
  .rule { position: absolute; height: 1px; background: rgba(255,255,255,0.55); }

  .benefits { position: absolute; display: grid; grid-template-columns: auto auto; list-style: none; font-weight: 500; white-space: nowrap; line-height: 1; }
  .benefits li { display: flex; align-items: center; }
  .chevrons { flex: none; margin-right: 0.4em; width: 0.8em; height: 0.6em; }

  .cta-badge { position: absolute; border-radius: 50%; background: radial-gradient(circle at 40% 35%, #ee6a6e 0%, var(--red) 45%, var(--red-dark) 100%); box-shadow: 0 4px 10px rgba(0,0,0,0.35); display: flex; align-items: center; justify-content: center; }
  .cta-text { transform: rotate(-16deg); text-align: center; line-height: 1.05; font-weight: 500; }
  .cta-text strong { font-weight: 700; display: block; }

  .event-icon { position: absolute; left: 122px; top: 259px; width: 158px; height: 157px; background: linear-gradient(135deg, #2a69b3, var(--navy)); border: 1px solid #5b86bf; display: flex; align-items: center; justify-content: center; font-weight: 600; font-size: 19px; }

  /* header */
  .header .wordmark { left: 555px; top: 50px; font-size: 78px; }
  .header .tagline { left: 556px; top: 131px; font-size: 23px; }
  .header .rule { left: 556px; top: 167px; width: 545px; }
  .header .benefits { left: 556px; top: 185px; font-size: 19px; column-gap: 52px; row-gap: 10px; }
  .header .cta-badge { left: 314px; top: 75px; width: 178px; height: 178px; font-size: 22px; }

  /* 600x250 */
  .mega-desktop .wordmark { left: 123px; top: 30px; font-size: 68px; }
  .mega-desktop .tagline { left: 123px; top: 106px; font-size: 21px; }
  .mega-desktop .rule { left: 123px; top: 138px; width: 490px; }
  .mega-desktop .benefits { left: 123px; top: 152px; font-size: 17px; column-gap: 48px; row-gap: 9px; }
  .mega-desktop .cta-badge { left: 610px; top: 179px; width: 124px; height: 124px; font-size: 15px; }

  /* 400x300 */
  .mega-mobile .wordmark { left: 19px; top: 24px; font-size: 62px; }
  .mega-mobile .tagline { left: 19px; top: 91px; font-size: 19px; }
  .mega-mobile .rule { left: 19px; top: 125px; width: 455px; }
  .mega-mobile .benefits { left: 19px; top: 144px; font-size: 15px; column-gap: 48px; row-gap: 10px; }
  .mega-mobile .cta-badge { left: 333px; top: 211px; width: 138px; height: 138px; font-size: 16px; }
</style>
</head>
<body>

<svg width="0" height="0" style="position:absolute">
  <defs>
    <symbol id="double-chevron" viewBox="0 0 16 12">
      <path d="M1 1l5 5-5 5M8 1l5 5-5 5" fill="none" stroke="#36a9ea" stroke-width="2"/>
    </symbol>
    <linearGradient id="blue-field" x1="0" y1="0" x2="1" y2="1">
      <stop offset="0" stop-color="#0a2560"/>
      <stop offset="0.6" stop-color="#103f86"/>
      <stop offset="1" stop-color="#1f78c2"/>
    </linearGradient>
    <linearGradient id="hall-photo" x1="0" y1="0" x2="0" y2="1">
      <stop offset="0" stop-color="#a9bfd8"/>
      <stop offset="0.55" stop-color="#d9c3b2"/>
      <stop offset="1" stop-color="#b98367"/>
    </linearGradient>
    <linearGradient id="hall-fade" x1="0" y1="0" x2="0" y2="1">
      <stop offset="0" stop-color="#0c2d6a"/>
      <stop offset="0.45" stop-color="#1d5fa8"/>
      <stop offset="0.75" stop-color="#b4c4d8"/>
      <stop offset="1" stop-color="#c08a6c"/>
    </linearGradient>
  </defs>
</svg>

<!-- Event page header -->
<section class="banner header">
  <svg class="banner-bg" viewBox="0 0 1200 382" preserveAspectRatio="none">
    <rect width="1200" height="382" fill="url(#blue-field)"/>
    <polygon points="0,0 470,0 278,372 0,372" fill="url(#hall-photo)" role="img" aria-label="Foto: Publikum in einem Konferenzsaal vor einer Leinwand"/>
    <polygon points="440,0 470,0 278,372 248,372" fill="#e9eef5"/>
    <rect y="372" width="1200" height="10" fill="var(--band)"/>
  </svg>
  <div class="cta-badge"><p class="cta-text">SICHERN SIE<br>SICH IHRE<strong>TEILNAHME</strong></p></div>
  <div class="wordmark"><span class="wordmark-square"></span>VOLMARKTIS</div>
  <p class="tagline">EXPO FOR DIGITAL BUSINESS - LIFE IS DIGITAL</p>
  <div class="rule"></div>
  <ul class="benefits">
    <li><svg class="chevrons"><use href="#double-chevron"/></svg>Kostengünstige Teilnahme</li>
    <li><svg class="chevrons"><use href="#double-chevron"/></svg>Größere Reichweite</li>
    <li><svg class="chevrons"><use href="#double-chevron"/></svg>Keine Reiseaufwendungen</li>
    <li><svg class="chevrons"><use href="#double-chevron"/></svg>Größere Skalierbarkeit</li>
  </ul>
</section>

<!-- Event page icon -->
<div class="event-icon">VOLMARKTIS</div>

<!-- Megabanner desktop -->
<section class="banner mega-desktop">
  <svg class="banner-bg" viewBox="0 0 740 308" preserveAspectRatio="none">
    <rect width="740" height="308" fill="url(#hall-fade)" role="img" aria-label="Foto: Konferenzsaal mit Publikum, nach oben in Blau überblendet"/>
    <polygon points="0,0 70,0 0,110" fill="#d7e1ee" opacity="0.85"/>
    <polygon points="70,0 92,0 0,150 0,110" fill="#ffffff" opacity="0.5"/>
    <polygon points="740,110 740,150 680,250 655,250" fill="#ffffff" opacity="0.5"/>
  </svg>
  <div class="wordmark"><span class="wordmark-square"></span>VOLMARKTIS</div>
  <p class="tagline">EXPO FOR DIGITAL BUSINESS - LIFE IS DIGITAL</p>
  <div class="rule"></div>
  <ul class="benefits">
    <li><svg class="chevrons"><use href="#double-chevron"/></svg>Kostengünstige Teilnahme</li>
    <li><svg class="chevrons"><use href="#double-chevron"/></svg>Größere Reichweite</li>
    <li><svg class="chevrons"><use href="#double-chevron"/></svg>Keine Reiseaufwendungen</li>
    <li><svg class="chevrons"><use href="#double-chevron"/></svg>Größere Skalierbarkeit</li>
  </ul>
  <div class="cta-badge"><p class="cta-text">SICHERN SIE<br>SICH IHRE<strong>TEILNAHME</strong></p></div>
</section>

<!-- Megabanner mobile -->
<section class="banner mega-mobile">
  <svg class="banner-bg" viewBox="0 0 493 370" preserveAspectRatio="none">
    <rect width="493" height="370" fill="url(#hall-fade)" role="img" aria-label="Foto: Konferenzsaal mit Publikum, nach oben in Blau überblendet"/>
    <polygon points="493,110 493,150 430,260 405,260" fill="#ffffff" opacity="0.45"/>
  </svg>
  <div class="wordmark"><span class="wordmark-square"></span>VOLMARKTIS</div>
  <p class="tagline">EXPO FOR DIGITAL BUSINESS - LIFE IS DIGITAL</p>
  <div class="rule"></div>
  <ul class="benefits">
    <li><svg class="chevrons"><use href="#double-chevron"/></svg>Kostengünstige Teilnahme</li>
    <li><svg class="chevrons"><use href="#double-chevron"/></svg>Größere Reichweite</li>
    <li><svg class="chevrons"><use href="#double-chevron"/></svg>Keine Reiseaufwendungen</li>
    <li><svg class="chevrons"><use href="#double-chevron"/></svg>Größere Skalierbarkeit</li>
  </ul>
  <div class="cta-badge"><p class="cta-text">SICHERN SIE<br>SICH IHRE<strong>TEILNAHME</strong></p></div>
</section>

</body>
</html>
```